ReDesign CBD Packaging Box with needed Details and Pizazzz!

I have 3 things that need to be accomplished for this project to be completed.
1- Each box contains CBD oil in values of 500mg, 1500mg and 2500mg. Each value as a flavor as well. We offer 4 "Flavors": Natural (flavorless), Mint, Dragonfruit and Watermelon in the 3 variants listed above. So need a box for each.
2- After reviewing the design recently, I decided I am not as happy as I thought. So, I am open to any modifications that may make is shine and spark that says "buy me" figuratively.
3- The box should be easy to identify in terms of the amount of CBD and flavor it is. Play with colors maybe where the swirl is white is it is 2500mg, and gray if 1500mg and dark gray for 500mg? Something like that as an example but I am sure you have better ideas than I .

So to summarize, need to update the box with all the wording and information required to be on the box.

I am attaching:
1)the text that should be on the box in case you need it
2) the logo,
3)a version that i tried to making called "dragon fruit tincture 1500mg",
4)the original design packaging called "soapy packaging".
5)the template I am supposed to use.

Target Market(s)

Health and Nutrition, Sports, Alternative Medicine, Elderly,

Industry/Entity Type

Retail online

Requirements
Must have
• clear writing with clear font
Nice to have
• some color or absence of black maybe.
Should not have
• unnecessary images or too busy

```html
<!DOCTYPE html>
<html lang="en">
<head>
<meta charset="utf-8">
<title>Lather Lane CBD Oil – Dragon Fruit Carton</title>
<link rel="stylesheet" href="https://fonts.googleapis.com/css2?family=Barlow:ital,wght@0,400;0,500;0,600;0,700;1,400;1,500&family=Oswald:wght@400;500;700&family=Montserrat:wght@700;800&display=swap">
<style>
:root{
  --bg:#e6e6e6;
  --purple:#6e2c86;
  --purple-soft:#a771bd;
  --ink:#1a1a1a;
  --band:#111111;
  --paper:#ffffff;
  --bleed:#29a8e0;
  --cut:#e3161b;
  --safe:#1aa14a;
  --paste:#ffcc00;
  --dim:#e3161b;
}
*{margin:0;padding:0;box-sizing:border-box}
html,body{width:1200px;height:2395px;overflow:hidden;background:var(--bg)}
body{position:relative;font-family:"Barlow",Arial,sans-serif;color:var(--ink)}
.abs{position:absolute}

/* ---------- flat front panel ---------- */
.front{position:absolute;top:119px;width:270px;height:855px;background:var(--paper);box-shadow:0 6px 18px rgba(0,0,0,.12)}
.front--a{left:203px}
.front--b{left:613px}
.brand{position:absolute;display:flex;align-items:center;justify-content:center;border:2px solid var(--purple);border-radius:50%}
.brand__name{font-family:"Barlow",Arial,sans-serif;font-weight:700;color:var(--ink);white-space:nowrap}
.front .brand{left:75px;top:55px;width:120px;height:120px}
.front .brand__name{font-size:24px}
.pattern{position:absolute;background:radial-gradient(circle at 30% 30%,#ffffff 0 18%,#c9a3d8 40%,#7d3c96 70%,#ffffff 100%)}
.front .pattern{left:22px;top:191px;width:103px;height:425px}
.strip{position:absolute;background:var(--purple);color:#fff;text-align:center;overflow:hidden}
.front .strip{left:125px;top:191px;width:125px;height:425px}
.strip__title{display:inline-block;font-family:"Oswald",sans-serif;font-weight:700;writing-mode:vertical-rl;transform:rotate(180deg);white-space:nowrap;line-height:1}
.front .strip__title{font-size:82px;margin-top:22px}
.strip__sub{font-family:"Oswald",sans-serif;font-weight:400;line-height:1.35}
.front .strip__sub{font-size:16px;margin-top:20px}
.strip__dose{font-family:"Oswald",sans-serif;font-weight:500;line-height:1.2}
.front .strip__dose{font-size:19px;margin-top:16px}
.strip__dose small{display:block;font-weight:400}
.front .strip__dose small{font-size:14px}
.drop{position:absolute}
.flavor{position:absolute;font-family:"Montserrat",sans-serif;font-weight:800;color:var(--purple);text-align:center;line-height:1.05}
.front .flavor{left:20px;top:655px;width:170px;font-size:24px}
.seal{position:absolute;border-radius:50%;border:2px solid var(--ink);background:var(--paper)}
.seal::after{content:"";position:absolute;inset:22%;border-radius:50%;background:var(--ink)}
.certified{position:absolute;font-family:"Montserrat",sans-serif;font-weight:700;color:var(--purple);letter-spacing:.14em;text-align:center}
.front .certified{left:0;width:270px;top:780px;font-size:14px}
.volume{position:absolute;left:0;bottom:0;width:100%;background:var(--band);color:#fff;text-align:center;font-weight:400}
.front .volume{height:50px;line-height:50px;font-size:17px}

/* ---------- dimensions ---------- */
.dim-label{position:absolute;font-family:Arial,Helvetica,sans-serif;font-weight:700;color:var(--dim);font-size:28px;text-align:center;white-space:nowrap}
.dim-label--v{transform:rotate(90deg);transform-origin:center}

/* ---------- dieline panel copy ---------- */
.panel{position:absolute;top:1480px;width:141px;height:460px;text-align:center}
.panel h3{font-family:"Barlow",sans-serif;font-weight:700;color:var(--purple);font-size:12px;margin-top:8px;line-height:1.1}
.panel p{font-size:9.6px;line-height:1.28}
.panel p.italic{font-style:italic;font-weight:500}
.panel p.bold{font-weight:600}
.band-text{position:absolute;top:1952px;height:30px;line-height:30px;width:167px;text-align:center;color:#fff;font-size:11px;white-space:nowrap}
.ornament{display:block;margin:8px auto 0;width:12px;height:16px;border-radius:50% 50% 45% 45%;background:var(--purple-soft)}
.spectrum-rule{display:flex;align-items:center;justify-content:center;gap:5px;font-family:"Oswald",sans-serif;font-size:12px}
.spectrum-rule::before,.spectrum-rule::after{content:"";width:20px;height:1px;background:var(--ink)}
.tincture{font-family:"Oswald",sans-serif;font-weight:500;color:var(--purple);font-size:25px;line-height:1.1;white-space:nowrap}
.heading-cbd{font-family:"Montserrat",sans-serif;font-weight:800;color:var(--purple);font-size:25px;margin-top:30px}
.claim-box{margin:10px auto 0;width:108px;border:1.5px solid var(--purple);padding:4px 0;font-family:"Oswald",sans-serif;font-weight:500;font-size:19px;line-height:1.08;color:var(--ink)}
.claim-box span{color:var(--purple);display:block}

/* mini front inside dieline */
.mini .brand{left:674px;top:1497px;width:76px;height:76px}
.mini .brand__name{font-size:14px}
.mini .pattern{left:641px;top:1580px;width:71px;height:255px}
.mini .strip{left:712px;top:1580px;width:70px;height:255px}
.mini .strip__title{font-size:48px;margin-top:12px}
.mini .strip__sub{font-size:9.5px;margin-top:10px}
.mini .strip__dose{font-size:10.5px;margin-top:10px}
.mini .strip__dose small{font-size:8px}
.mini .flavor{left:644px;top:1852px;width:90px;font-size:14px}
.mini .certified{left:628px;width:167px;top:1933px;font-size:8.5px}

/* lid brand */
.lid-brand{position:absolute;left:336px;top:1332px;width:86px;height:86px;transform:rotate(180deg)}
.lid-brand .brand__name{font-size:15px}

/* glue area */
.glue{position:absolute;left:256px;top:1478px;width:26px;height:470px;background:var(--paste)}
.glue-label{position:absolute;left:236px;top:1640px;width:70px;height:170px;font-family:Arial,Helvetica,sans-serif;font-size:19px;color:var(--ink);writing-mode:vertical-rl;white-space:nowrap;text-align:center;line-height:70px}

/* legend */
.legend-swatch{position:absolute;width:58px;height:15px}
.legend-text{position:absolute;font-family:Arial,Helvetica,sans-serif;font-weight:700;font-size:20px;line-height:20px;white-space:nowrap}
.spec{position:absolute;left:33px;top:2310px;font-family:Arial,Helvetica,sans-serif;font-weight:700;font-size:36px;color:var(--ink);letter-spacing:-.01em;white-space:nowrap}
</style>
</head>
<body>

<section class="front front--a">
  <div class="brand"><span class="brand__name">Lather Lane</span></div>
  <div class="pattern" role="img" aria-label="Dragon fruit slice pattern in purple and black seeds"></div>
  <div class="strip">
    <div class="strip__title">CBD OIL</div>
    <div class="strip__sub">Full Spectrum<br>CBD TINTURE</div>
    <div class="strip__dose">2500 MG CBD<small>42ML CBD PER ML</small></div>
  </div>
  <svg class="drop" style="left:161px;top:615px" width="58" height="96" viewBox="0 0 58 96"><path d="M24 0h10v18C34 30 58 50 58 67a29 29 0 0 1-58 0C0 50 24 30 24 18Z" fill="var(--purple)"/></svg>
  <div class="flavor">DRAGON<br>FRUIT</div>
  <div class="seal" style="left:70px;top:718px;width:56px;height:56px"></div>
  <div class="seal" style="left:145px;top:718px;width:56px;height:56px"></div>
  <div class="certified">CERTIFIED</div>
  <div class="volume">2 fl.oz. | 59.1471ml</div>
</section>

<section class="front front--b">
  <div class="brand"><span class="brand__name">Lather Lane</span></div>
  <div class="pattern" role="img" aria-label="Dragon fruit slice pattern in purple and black seeds"></div>
  <div class="strip">
    <div class="strip__title">CBD OIL</div>
    <div class="strip__sub">Full Spectrum<br>CBD TINTURE</div>
    <div class="strip__dose">2500 MG CBD<small>42ML CBD PER ML</small></div>
  </div>
  <svg class="drop" style="left:161px;top:615px" width="58" height="96" viewBox="0 0 58 96"><path d="M24 0h10v18C34 30 58 50 58 67a29 29 0 0 1-58 0C0 50 24 30 24 18Z" fill="var(--purple)"/></svg>
  <div class="flavor">DRAGON<br>FRUIT</div>
  <div class="seal" style="left:70px;top:718px;width:56px;height:56px"></div>
  <div class="seal" style="left:145px;top:718px;width:56px;height:56px"></div>
  <div class="certified">CERTIFIED</div>
  <div class="volume">2 fl.oz. | 59.1471ml</div>
</section>

<svg class="abs" style="left:0;top:0" width="1200" height="2395" viewBox="0 0 1200 2395">
  <g stroke="var(--dim)" stroke-width="1.5" fill="none">
    <path d="M295 1126H962M295 1119v14M462 1119v14M628 1119v14M795 1119v14M962 1119v14"/>
    <path d="M1060 1461V1985M1053 1461h14M1053 1985h14"/>
  </g>

  <g class="dieline">
    <path d="M283 1461V1262a36 36 0 0 1 36-36h118a36 36 0 0 1 36 36v199Z" fill="var(--paper)" stroke="var(--bleed)" stroke-width="1.5"/>
    <path d="M295 1461V1268a26 26 0 0 1 26-26h115a26 26 0 0 1 26 26v193" fill="none" stroke="var(--cut)" stroke-width="1.2"/>
    <path d="M295 1293H462" stroke="var(--cut)" stroke-width="1.2"/>
    <rect x="308" y="1254" width="141" height="26" rx="10" fill="none" stroke="var(--safe)" stroke-width="1.2"/>
    <rect x="308" y="1306" width="141" height="142" fill="none" stroke="var(--safe)" stroke-width="1.2"/>
    <path d="M462 1461V1392a26 26 0 0 1 26-26h85l32 40 18 55Z" fill="var(--paper)" stroke="var(--bleed)" stroke-width="1.5"/>
    <path d="M472 1461V1398a20 20 0 0 1 20-20h76l28 36 14 47" fill="none" stroke="var(--cut)" stroke-width="1.2"/>
    <path d="M488 1388h80l22 28 20 30H488Z" fill="none" stroke="var(--safe)" stroke-width="1.2"/>
    <path d="M795 1461l17-55a60 60 0 0 1 48-40h114v95Z" fill="var(--paper)" stroke="var(--bleed)" stroke-width="1.5"/>
    <path d="M805 1461l14-48a48 48 0 0 1 42-35h101v83" fill="none" stroke="var(--cut)" stroke-width="1.2"/>
    <path d="M822 1446l12-40a36 36 0 0 1 32-18h81v58Z" fill="none" stroke="var(--safe)" stroke-width="1.2"/>
    <path d="M228 1466L295 1441V1985H228Z" fill="var(--paper)" stroke="var(--bleed)" stroke-width="1.5"/>
    <path d="M240 1474L295 1455" stroke="var(--cut)" stroke-width="1.2"/>
    <rect x="295" y="1461" width="680" height="524" fill="var(--paper)" stroke="var(--bleed)" stroke-width="1.5"/>
    <rect x="228" y="1950" width="747" height="35" fill="var(--band)"/>
    <path d="M295 1985h167l-12 56v78H288v-80Z" fill="var(--band)"/>
    <path d="M462 1985h166l-44 80H470Z" fill="var(--band)"/>
    <path d="M628 1985h167l-12 56v78H621v-80Z" fill="var(--band)"/>
    <path d="M795 1985h180l-20 30-36 60H800Z" fill="var(--band)"/>
    <g fill="none" stroke="var(--safe)" stroke-width="1.2">
      <path d="M315 2000h125v90l-40-28-22 28h-4l-16-50-19 50h-24Z"/>
      <path d="M480 2000h135l-40 55H484Z"/>
      <path d="M648 2000h125v90l-40-28-22 28h-4l-16-50-19 50h-24Z"/>
      <path d="M812 2000h135l-40 55H816Z"/>
      <rect x="308" y="1474" width="141" height="471"/>
      <rect x="475" y="1474" width="140" height="471"/>
      <rect x="641" y="1474" width="141" height="471"/>
      <rect x="808" y="1474" width="141" height="471"/>
    </g>
    <g fill="none" stroke="var(--cut)" stroke-width="1.2">
      <path d="M295 1461V1985M462 1461V1985M628 1461V1985M795 1461V1985M962 1461V1985"/>
      <path d="M240 1474V1960H962M295 1461H962"/>
      <path d="M300 1985v120h158v-75l8-45M470 1990l14 70h96l40-70M632 1985v120h158v-75l8-45M800 1990l6 70h132l25-70"/>
    </g>
  </g>
</svg>

<div class="dim-label" style="left:295px;top:1084px;width:167px">1.58 ”</div>
<div class="dim-label" style="left:462px;top:1084px;width:166px">1.58 ”</div>
<div class="dim-label" style="left:628px;top:1084px;width:167px">1.58 ”</div>
<div class="dim-label" style="left:795px;top:1084px;width:167px">1.58 ”</div>
<div class="dim-label dim-label--v" style="left:1033px;top:1704px;width:100px">4.95 ”</div>

<div class="brand lid-brand"><span class="brand__name">Lather Lane</span></div>

<div class="glue"></div>
<div class="glue-label">GLUED AREA</div>

<div class="panel" style="left:308px">
  <h3>INGREDIENTS</h3>
  <p class="italic">Organic Non-GMO Coconut Oil, Certified Vegan and High Quality Full Spectrum CBD.</p>
  <h3 style="margin-top:14px">DIRECTIONS</h3>
  <p class="italic">Recommended dosage is 0.25mg CBD multiplied by your body weight, in pounds, on a daily basis.</p>
  <div class="brand" style="position:relative;margin:14px auto 0;width:80px;height:80px"><span class="brand__name" style="font-size:14px">Lather Lane</span></div>
  <h3 style="margin-top:14px">WARNINGS</h3>
  <p>Contains Tree Nuts (Coconut); Consult your doctor before use; Discontinue use if any adverse reactions occur. Do not use it if the tamper seal is broken.</p>
  <h3 style="margin-top:12px">CONTACT</h3>
  <p class="bold">Lather Lane<br>Bayview, CA 90000<br>(555) 010-0199<br>info@latherlane.com</p>
</div>
<div class="band-text" style="left:295px">www.latherlane.com</div>

<div class="panel" style="left:475px;width:140px">
  <p class="italic" style="margin-top:8px">Indulge our coconut oil infused CBD oil. Carefully crafted to bring you the soothing benefits of CBD, the oil is made from organic coconut oil that is Non-GMO, Certified Vegan, and features flavorings all infused with the high quality, full-spectrum, CBD oil. Each bottle contains a generous two ounces. Treat yourself to the purity of organic coconut based CBD oil and unwind with its incredible calming effects.*</p>
  <span class="ornament" role="img" aria-label="Small dragon fruit icon"></span>
  <h3 style="margin-top:20px">DISCLAIMER</h3>
  <p>These statements have not been evaluated by the Food and Drug Administration. These products are not intended to diagnose, treat, cure, or prevent any disease.</p>
  <div class="spectrum-rule" style="margin-top:24px">Full Spectrum</div>
  <div class="tincture">CBD TINTURE</div>
</div>
<div class="band-text" style="left:462px;width:166px">2 fl.oz. | 59.1471ml</div>

<div class="mini">
  <div class="brand"><span class="brand__name">Lather Lane</span></div>
  <div class="pattern" role="img" aria-label="Dragon fruit slice pattern in purple and black seeds"></div>
  <div class="strip">
    <div class="strip__title">CBD OIL</div>
    <div class="strip__sub">Full Spectrum<br>CBD TINTURE</div>
    <div class="strip__dose">2500 MG CBD<small>42ML CBD PER ML</small></div>
  </div>
  <svg class="drop" style="left:732px;top:1834px" width="32" height="54" viewBox="0 0 58 96"><path d="M24 0h10v18C34 30 58 50 58 67a29 29 0 0 1-58 0C0 50 24 30 24 18Z" fill="var(--purple)"/></svg>
  <div class="flavor">DRAGON<br>FRUIT</div>
  <div class="seal" style="left:670px;top:1895px;width:34px;height:34px"></div>
  <div class="seal" style="left:716px;top:1895px;width:34px;height:34px"></div>
  <div class="certified">CERTIFIED</div>
</div>
<div class="band-text" style="left:628px">2 fl.oz. | 59.1471ml</div>

<div class="panel" style="left:808px">
  <div class="heading-cbd">CBD OIL</div>
  <p style="margin-top:8px">Lather Lane uses a third (3rd) party laboratory to ensure customers receive a pure and safe product.</p>
  <p style="margin-top:14px">Testing analysis reviews the following: Cannabinoid Profiles &amp; Potency, Heavy Metal Analysis, Microbiological Contaminants (like mold), Volatile Organic Compounds and Pesticides.</p>
  <span class="ornament" style="margin-top:22px" role="img" aria-label="Small dragon fruit icon"></span>
  <div class="claim-box" style="margin-top:24px">ALL NATURAL<br>AND VEGAN<span>CERTIFIED</span></div>
  <p class="italic" style="margin-top:40px;font-size:11px">Visit Our website<br>for more information.</p>
  <p class="italic" style="margin-top:6px;font-size:10.5px;color:var(--purple)">www.latherlane.com</p>
</div>
<div class="band-text" style="left:795px">2 fl.oz. | 59.1471ml</div>

<div class="spec">DIMENSIONS: 1.58 x 1.58 x 4.95”</div>
<div class="legend-swatch" style="left:747px;top:2304px;background:var(--bleed)"></div>
<div class="legend-text" style="left:813px;top:2301px;color:var(--bleed)">BLEED AREA</div>
<div class="legend-swatch" style="left:747px;top:2330px;background:var(--safe)"></div>
<div class="legend-text" style="left:813px;top:2327px;color:var(--safe)">SAFE AREA</div>
<div class="legend-swatch" style="left:955px;top:2304px;background:var(--cut)"></div>
<div class="legend-text" style="left:1019px;top:2301px;color:var(--cut)">CUTTING AREA</div>
<div class="legend-swatch" style="left:955px;top:2330px;background:var(--paste)"></div>
<div class="legend-text" style="left:1019px;top:2327px;color:var(--paste)">PASTING AREA</div>

</body>
</html>
```